Willowmere Loft B&B Business Card

This beautiful high-class B&B is looking for a business card that stands out from the rest. They are in the middle of the countryside, have chickens, geese and a dog. They also love bumble bees.

I was maybe thinking a rustic drawing / print of a bumble bee and a sketch of the house, I am not sure.. I quite like the feel of this... http://www.tarnwick-mill.co.uk/

Industry/Entity Type

Business

Contact Information for Business Card

Willowmere Loft
Bed & Breakfast
Brackleford, Hensworth, Somerset, TA14 7QP
01632 960418 | www.willowmereloft.co.uk

```html
<!DOCTYPE html>
<html lang="en">
<head>
<meta charset="utf-8">
<title>Willowmere Loft B&amp;B Business Card</title>
<link rel="stylesheet" href="https://fonts.googleapis.com/css2?family=Cinzel:wght@400&family=Open+Sans:wght@400;700&display=swap">
<style>
  :root {
    --orange: #f26722;
    --grey: #a7a9ac;
    --grey-text: #808285;
    --white: #ffffff;
    --page: #ecebe8;
    --sky: #6fa7dc;
    --stone: #d9cdb0;
    --lawn: #5f8a35;
  }
  html, body {
    margin: 0;
    width: 1200px;
    height: 900px;
    overflow: hidden;
    background: var(--page);
  }
  .canvas { position: relative; width: 1200px; height: 900px; }

  .card-front {
    position: absolute;
    left: 150px; top: 72px;
    width: 590px; height: 365px;
    background: var(--white);
    overflow: hidden;
    box-shadow: 0 4px 14px rgba(0,0,0,.12);
    font-family: "Open Sans", sans-serif;
  }
  .card-bands { position: absolute; inset: 0; }

  .brand {
    position: absolute;
    left: 0; right: 0; top: 70px;
    text-align: center;
  }
  .brand-name {
    margin: 0;
    font-family: "Cinzel", serif;
    font-weight: 400;
    font-size: 46px;
    line-height: 1;
    color: var(--orange);
    letter-spacing: 1px;
  }
  .brand-tagline {
    display: flex;
    align-items: center;
    justify-content: center;
    gap: 10px;
    margin-top: 6px;
    font-size: 14px;
    font-weight: 700;
    letter-spacing: 6px;
    color: var(--grey-text);
  }
  .brand-tagline::before, .brand-tagline::after {
    content: "";
    width: 60px;
    height: 1px;
    background: var(--grey-text);
  }

  .person {
    position: absolute;
    left: 0; right: 0; top: 238px;
    text-align: center;
    color: var(--white);
  }
  .person-name { margin: 0; font-size: 24px; font-weight: 700; line-height: 1.2; }
  .person-role { margin: 0; font-size: 15px; line-height: 1.3; }

  .contact {
    position: absolute;
    top: 298px; left: 0; right: 0;
    display: flex;
    justify-content: center;
    color: var(--white);
    font-size: 15px;
    line-height: 22px;
  }
  .contact-address { text-align: right; padding-right: 18px; margin: 0; font-style: normal; }
  .contact-lines { padding-left: 18px; border-left: 1px solid var(--white); }
  .contact-line { display: flex; align-items: center; gap: 6px; margin: 0; }
  .contact-line svg { width: 14px; height: 14px; fill: var(--white); }

  .card-back {
    position: absolute;
    left: 388px; top: 505px;
    width: 567px; height: 352px;
    background: linear-gradient(180deg, var(--sky) 0%, #a9c8e6 20%, var(--stone) 32%, #cbbd9c 58%, var(--lawn) 62%, #4d7a2a 100%);
    box-shadow: 0 4px 14px rgba(0,0,0,.12);
  }
</style>
</head>
<body>
<main class="canvas">
  <section class="card-front">
    <svg class="card-bands" viewBox="0 0 590 365" width="590" height="365" aria-hidden="true">
      <polygon points="0,195 405,195 381,221 0,221" fill="var(--grey)"/>
      <polygon points="0,224 387,224 418,186 590,186 590,365 0,365" fill="var(--orange)"/>
    </svg>

    <div class="brand">
      <h1 class="brand-name">Willowmere Loft</h1>
      <div class="brand-tagline">BED &amp; BREAKFAST</div>
    </div>

    <div class="person">
      <p class="person-name">Daniel Hartley</p>
      <p class="person-role">Managing Director</p>
    </div>

    <div class="contact">
      <address class="contact-address">Brackleford, Hensworth,<br>Somerset, TA14 7QP</address>
      <div class="contact-lines">
        <p class="contact-line">
          <svg viewBox="0 0 24 24"><path d="M6.6 10.8a15.1 15.1 0 0 0 6.6 6.6l2.2-2.2a1 1 0 0 1 1-.25 11.4 11.4 0 0 0 3.6.57 1 1 0 0 1 1 1V20a1 1 0 0 1-1 1A17 17 0 0 1 3 4a1 1 0 0 1 1-1h3.5a1 1 0 0 1 1 1c0 1.25.2 2.45.57 3.57a1 1 0 0 1-.25 1z"/></svg>
          01632 960418
        </p>
        <p class="contact-line">
          <svg viewBox="0 0 24 24"><path d="M12 2a10 10 0 1 0 0 20 10 10 0 0 0 0-20zm6.9 6h-2.9a15.6 15.6 0 0 0-1.4-3.6A8 8 0 0 1 18.9 8zM12 4a14 14 0 0 1 1.9 4h-3.8A14 14 0 0 1 12 4zM4.3 14a8 8 0 0 1 0-4h3.4a16.5 16.5 0 0 0 0 4zm.8 2h2.9a15.6 15.6 0 0 0 1.4 3.6A8 8 0 0 1 5.1 16zM8 8H5.1a8 8 0 0 1 4.3-3.6A15.6 15.6 0 0 0 8 8zm4 12a14 14 0 0 1-1.9-4h3.8A14 14 0 0 1 12 20zm2.3-6H9.7a14.7 14.7 0 0 1 0-4h4.6a14.7 14.7 0 0 1 0 4zm.3 5.6a15.6 15.6 0 0 0 1.4-3.6h2.9a8 8 0 0 1-4.3 3.6zm1.7-5.6a16.5 16.5 0 0 0 0-4h3.4a8 8 0 0 1 0 4z"/></svg>
          www.willowmereloft.co.uk
        </p>
      </div>
    </div>
  </section>

  <section class="card-back" role="img" aria-label="Photograph of the stone barn guesthouse with a red tiled roof and arched window, two hens walking on the lawn in front"></section>
</main>
</body>
</html>
```